Tickle Your Toes! Summer One Act Festival

I need a poster design for a summer festival of short comedy plays in San Francisco, all with a historical or intellectual theme! From Ancient Greece to the Russian Revolution to Cold War Politics to College Admissions! The target audience demographic is 20-30 year old San Francisco "hipster types" who will be attending a food truck festival. The festival performance dates are Friday evenings, July 22 to August 15! We would like a clever, antique looking design that conveys comedy and history. We would also like the names of the plays, all by the same author, Milo Fairbank, on the poster as well! The titles are:

Vexilla
Gin and Quibbles
The Endless Oboe Concerto
Quill Snap
Lighthouse Deliberations
Pigeons Hold a Vote

```html
<!DOCTYPE html>
<html lang="en">
<head>
<meta charset="utf-8">
<title>Tickle Your Toes! Summer One Act Festival</title>
<link href="https://fonts.googleapis.com/css2?family=Sancreek&family=Lobster&family=Oswald:wght@400;500&family=Alfa+Slab+One&family=Pinyon+Script&display=swap" rel="stylesheet">
<style>
  :root {
    --sky: #4a8fb6;
    --sky-deep: #3f86b0;
    --mustard: #e0b73b;
    --paper: #ffffff;
    --collage-warm: #b88a5e;
    --collage-cool: #6f8f95;
    --collage-green: #5e7248;
  }
  * { margin: 0; padding: 0; box-sizing: border-box; }
  html, body { width: 928px; height: 1200px; overflow: hidden; background: var(--paper); }
  .poster { position: relative; width: 928px; height: 1200px; overflow: hidden; background: var(--mustard); }

  .masthead { position: absolute; left: 0; top: 0; width: 928px; height: 360px; background: var(--sky); }
  .title { position: absolute; left: 0; top: 66px; width: 928px; height: 140px; display: flex; justify-content: center; align-items: center; gap: 6px; font-weight: normal; }
  .title-word { display: inline-block; font-family: "Sancreek", serif; font-size: 118px; line-height: 1; color: var(--paper); transform: scaleY(2.05); transform-origin: center; }
  .title-badge { width: 140px; height: 140px; border-radius: 50%; background: var(--paper); display: flex; align-items: center; justify-content: center; font-family: "Lobster", cursive; font-size: 56px; color: var(--sky); flex-shrink: 0; }
  .subtitle { position: absolute; left: 0; top: 264px; width: 928px; text-align: center; font-family: "Lobster", cursive; font-size: 80px; color: var(--paper); line-height: 1; }

  .collage { position: absolute; left: 0; top: 360px; width: 928px; height: 333px; }

  .themes { position: absolute; left: -30px; top: 420px; width: 420px; height: 220px; background: var(--mustard); transform: rotate(-22deg); color: var(--paper); font-family: "Oswald", sans-serif; text-transform: uppercase; padding: 20px 30px 0 50px; line-height: 1; }
  .themes .l1 { font-size: 34px; }
  .themes .l2 { font-size: 50px; font-weight: 500; }
  .themes .l3 { font-size: 30px; text-align: right; padding-right: 10px; }
  .themes .l4 { font-size: 30px; }
  .themes .l5 { font-size: 24px; text-align: right; padding-right: 20px; }

  .byline-shape { position: absolute; left: 0; top: 0; width: 928px; height: 900px; }
  .byline { position: absolute; left: 575px; top: 380px; width: 275px; text-align: center; color: var(--paper); font-family: "Oswald", sans-serif; text-transform: uppercase; line-height: 1.12; font-size: 33px; }
  .byline .author { font-size: 40px; font-weight: 500; }

  .day { position: absolute; left: 48px; top: 728px; font-family: "Alfa Slab One", serif; font-size: 29px; letter-spacing: 3px; color: var(--paper); }
  .date-month { position: absolute; font-family: "Sancreek", serif; font-size: 100px; line-height: 1; color: var(--paper); transform: scale(0.9, 1.45); transform-origin: 0 0; }
  .date-num { position: absolute; font-family: "Pinyon Script", cursive; font-size: 112px; line-height: 1; color: var(--paper); }
  .date-to { position: absolute; left: 46px; top: 906px; font-family: "Alfa Slab One", serif; font-size: 24px; color: var(--paper); }
  .july { left: 30px; top: 764px; }
  .july-num { left: 222px; top: 762px; }
  .august { left: 30px; top: 938px; }
  .august-num { left: 340px; top: 936px; }
  .venue { position: absolute; left: 48px; top: 1108px; font-family: "Alfa Slab One", serif; font-style: normal; font-size: 19px; line-height: 1.35; color: var(--paper); }

  .plays { position: absolute; left: 495px; top: 754px; list-style: none; font-family: "Oswald", sans-serif; font-size: 40px; line-height: 61px; color: var(--paper); }
</style>
</head>
<body>
<main class="poster">
  <header class="masthead">
    <h1 class="title">
      <span class="title-word">TICKLE</span>
      <span class="title-badge">your</span>
      <span class="title-word">TOES!</span>
    </h1>
    <p class="subtitle">Summer One Act Festival</p>
  </header>

  <svg class="collage" viewBox="0 0 928 333" role="img" aria-label="Collage of historical imagery: ancient mosaic, old stamps and flags, ivy-covered campus building, old map and classical relief">
    <defs>
      <linearGradient id="collageTone" x1="0" y1="0" x2="1" y2="0.4">
        <stop offset="0" stop-color="#b88a5e"/>
        <stop offset="0.35" stop-color="#6f8f95"/>
        <stop offset="0.6" stop-color="#5e7248"/>
        <stop offset="1" stop-color="#b88a5e"/>
      </linearGradient>
    </defs>
    <rect width="928" height="333" fill="url(#collageTone)"/>
  </svg>

  <div class="themes">
    <div class="l1">From Ancient Greece</div>
    <div class="l2">to the Russian</div>
    <div class="l3">Revolution to</div>
    <div class="l4">Cold War Politics to</div>
    <div class="l5">College Admissions!</div>
  </div>

  <svg class="byline-shape" viewBox="0 0 928 900" aria-hidden="true">
    <polygon points="454,492 600,360 858,452 666,825" fill="var(--sky-deep)"/>
  </svg>
  <p class="byline">6 Original<br>Short Plays by<br><span class="author">Milo Fairbank</span></p>

  <p class="day">FRIDAY EVENINGS</p>
  <span class="date-month july">JULY</span>
  <span class="date-num july-num">22</span>
  <span class="date-to">TO</span>
  <span class="date-month august">AUGUST</span>
  <span class="date-num august-num">15</span>
  <address class="venue">Building K, Room 210,<br>Harbor Pavilion, San Francisco, CA</address>

  <ul class="plays">
    <li>Vexilla</li>
    <li>Gin and Quibbles</li>
    <li>The Endless Oboe Concerto</li>
    <li>Quill Snap</li>
    <li>Lighthouse Deliberations</li>
    <li>Pigeons Hold a Vote</li>
  </ul>
</main>
</body>
</html>
```